Website for SAAS Fleet Maintenance Software

We are looking to have a public website showing a fleet maintenance software SAAS similar to vornelta.com and trubask.com
the software must have a full complete public website and all content must be included, we will not supply the content. this is not for the actual solution, it is for the public facing website with all contents "About Fleet Maintenance software" similar to the websites above, we need at least 20 pages including the contents with industries etc.
Please send your proposal

Target Market(s)

Companies with a fleet of vehicles

Industry/Entity Type

Fleet Management

Coding

Coded - Design and coding required

Colors
0054AA
0677BA
7BADD7
CADEEF
E8F1F8
6B429C
8869AF
B7A5CE
E3DAEB
F3F0F8

Requirements
Must have
• Content must be provided by the freelancer

```html
<!DOCTYPE html>
<html lang="en">
<head>
<meta charset="utf-8">
<title>Routevia – Fleet Maintenance Software</title>
<link href="https://fonts.googleapis.com/css2?family=Montserrat:wght@700;800&family=Mulish:wght@400;600;700&display=swap" rel="stylesheet">
<style>
:root{
  --blue:#0054AA;
  --blue-2:#0677BA;
  --blue-3:#7BADD7;
  --blue-4:#CADEEF;
  --blue-5:#E8F1F8;
  --purple:#6B429C;
  --purple-2:#8869AF;
  --purple-3:#B7A5CE;
  --purple-4:#E3DAEB;
  --purple-5:#F3F0F8;
  --ink:#1d2a3a;
  --text:#3b3f46;
  --band:#f3f3f4;
  --line:#d9dbe0;
}
*{box-sizing:border-box;margin:0;padding:0}
html,body{width:1200px;height:4084px;overflow:hidden;background:#fff}
body{position:relative;font-family:"Mulish",sans-serif;color:var(--text)}
.abs{position:absolute}
.head{font-family:"Montserrat",sans-serif;font-weight:800;text-transform:uppercase;color:var(--blue);letter-spacing:.3px}
.rule{position:absolute;width:38px;height:3px;background:var(--ink)}
.body-copy{font-size:12.5px;line-height:19.2px;color:var(--text)}
.btn{position:absolute;display:flex;align-items:center;justify-content:center;background:var(--purple);color:#fff;font-size:14px;font-weight:600;border-radius:6px;text-decoration:none}
.art{position:absolute;border-radius:10px}

/* header */
.brand{position:absolute;display:flex;align-items:center;gap:10px;font-family:"Montserrat",sans-serif;font-weight:800;color:var(--blue);text-transform:uppercase}
.brand-dot{border-radius:50%;border:3px solid var(--blue);background:#fff}
.nav{position:absolute;left:396px;top:42px;display:flex;gap:31px;font-size:13.5px;color:var(--ink)}
.nav .current{color:var(--blue-2);font-weight:700;border-bottom:2px solid var(--blue-2);padding-bottom:5px}
.btn-demo{left:830px;top:35px;width:108px;height:35px;background:var(--blue);font-size:13px}
.btn-trial-top{left:954px;top:35px;width:113px;height:35px;font-size:13px}

/* partners */
.partners{position:absolute;left:130px;top:690px;width:937px;display:flex;justify-content:space-between}
.partner-badge{width:118px;height:44px;border-radius:6px;background:#e6e7ea}

/* features */
.band{position:absolute;left:0;width:1200px;background:var(--band)}
.feature{position:absolute;top:1843px;width:300px;text-align:center}
.feature svg{display:block;margin:0 auto}
.feature h3{font-family:"Montserrat",sans-serif;font-weight:700;font-size:17px;color:var(--ink);margin-top:44px}
.feature p{font-size:12.5px;line-height:19.2px;margin:16px auto 0;width:250px}
.divider{position:absolute;top:1832px;width:1px;height:310px;background:var(--line)}

/* blog */
.card{position:absolute;top:2820px;width:456px;height:529px;border:1px solid var(--line);background:#fff}
.card .art{left:40px;top:25px;width:376px;height:214px}
.card h4{position:absolute;left:45px;top:270px;width:370px;font-family:"Montserrat",sans-serif;font-weight:700;font-size:17px;line-height:24px;color:var(--ink)}
.card p{position:absolute;left:45px;top:335px;width:370px}
.card .btn{left:45px;top:450px;width:95px;height:34px;font-size:13px}

/* footer */
.footer-col h5{font-family:"Montserrat",sans-serif;font-weight:700;font-size:13px;color:var(--ink);letter-spacing:.4px}
.footer-col ul{list-style:none;margin-top:14px}
.footer-col li{font-size:12.5px;line-height:24px;color:var(--text)}
.social{display:flex;gap:19px;margin-top:17px}
.social span{width:35px;height:35px;border-radius:50%;display:block}
</style>
</head>
<body>

<header>
  <div class="brand" style="left:130px;top:30px;font-size:24px">
    <span class="brand-dot" style="width:54px;height:54px"></span>Routevia
  </div>
  <nav class="nav">
    <span class="current">Home</span><span>About Us</span><span>Products</span><span>Resources</span><span>Contact Us</span>
  </nav>
  <a class="btn btn-demo">Book a Demo</a>
  <a class="btn btn-trial-top">Start Free Trial</a>
</header>

<section class="hero">
  <h1 class="head abs" style="left:133px;top:166px;font-size:26px;line-height:33.5px;width:340px">
    Revolutionize your fleet maintenance <span style="color:var(--purple)">with our powerful SaaS solution</span>
  </h1>
  <p class="abs" style="left:133px;top:328px;width:270px;font-size:13.5px;line-height:22.5px;color:var(--ink)">Optimize fleet maintenance with our SAAS software. Increase efficiency, lower costs, and streamline operations. Try it now!</p>
  <a class="btn" style="left:133px;top:447px;width:133px;height:35px">Start Free Trial</a>
  <div class="art" role="img" aria-label="Illustration of two people presenting a fleet tracking map on a large monitor" style="left:452px;top:130px;width:615px;height:398px;background:linear-gradient(160deg,var(--blue-5),#dbe6ee 60%,#f6e3d2)"></div>
</section>

<section class="partners-section">
  <h2 class="head abs" style="left:0;width:1200px;text-align:center;top:600px;font-size:15px;color:var(--ink)">Our Partners</h2>
  <div class="rule" style="left:581px;top:640px"></div>
  <div class="partners">
    <span class="partner-badge"></span><span class="partner-badge"></span><span class="partner-badge"></span>
    <span class="partner-badge"></span><span class="partner-badge"></span><span class="partner-badge"></span>
  </div>
</section>

<section class="automate">
  <div class="art" role="img" aria-label="Illustration of a woman arranging task cards on a dashboard screen" style="left:95px;top:808px;width:505px;height:412px;background:linear-gradient(180deg,var(--blue-5),#eef1f4)"></div>
  <h2 class="head abs" style="left:666px;top:818px;width:340px;font-size:25px;line-height:33.5px">Maintaining your fleet shouldn't be complex - it ought to be automated.</h2>
  <div class="rule" style="left:666px;top:965px"></div>
  <p class="body-copy abs" style="left:666px;top:998px;width:405px">Sed ut perspiciatis unde omnis iste natus error sit voluptatem accusantium doloremque laudantium, totam rem aperiam, eaque ipsa quae ab illo inventore veritatis et quasi architecto beatae vitae dicta sunt explicabo. Nemo enim ipsam voluptatem quia voluptas sit aspernatur aut odit aut fugit, sed quia consequuntur magni dolores eos qui ratione voluptatem sequi nesciunt. Neque porro quisquam est, qui dolorem ipsum quia dolor sit amet, consectetur, adipisci velit, sed quia non numquam eius modi tempora incidunt ut labore et dolore magnam aliquam quaerat voluptatem</p>
  <a class="btn" style="left:669px;top:1205px;width:106px;height:39px">Read More</a>
</section>

<section class="data">
  <h2 class="head abs" style="left:131px;top:1326px;width:380px;font-size:25px;line-height:33.5px">Data is the lifeblood of your fleet's operations.</h2>
  <div class="rule" style="left:131px;top:1443px"></div>
  <p class="body-copy abs" style="left:131px;top:1479px;width:405px">Sed ut perspiciatis unde omnis iste natus error sit voluptatem accusantium doloremque laudantium, totam rem aperiam, eaque ipsa quae ab illo inventore veritatis et quasi architecto beatae vitae dicta sunt explicabo. Nemo enim ipsam voluptatem quia voluptas sit aspernatur aut odit aut fugit, sed quia consequuntur magni dolores eos qui ratione voluptatem sequi nesciunt. Neque porro quisquam est, qui dolorem ipsum quia dolor sit amet, consectetur, adipisci velit, sed quia non numquam eius modi tempora incidunt ut labore et dolore magnam aliquam quaerat voluptatem</p>
  <a class="btn" style="left:134px;top:1683px;width:106px;height:38px">Read More</a>
  <div class="art" role="img" aria-label="Illustration of a laptop showing fleet data charts with a truck and map pins" style="left:570px;top:1384px;width:516px;height:320px;background:linear-gradient(180deg,#eef2f6,var(--blue-4))"></div>
</section>

<section class="features">
  <div class="band" style="top:1780px;height:403px"></div>
  <div class="divider" style="left:425px"></div>
  <div class="divider" style="left:777px"></div>

  <div class="feature" style="left:105px">
    <svg width="80" height="80" viewBox="0 0 80 80" fill="none" stroke="var(--blue)" stroke-width="2.4" stroke-linecap="round">
      <circle cx="40" cy="30" r="16"/><circle cx="40" cy="27" r="5"/><path d="M31 40c2-5 16-5 18 0"/>
      <circle cx="24" cy="48" r="4"/><circle cx="56" cy="48" r="4"/><circle cx="40" cy="50" r="4"/>
      <path d="M16 72V62c0-4 4-6 8-6s8 2 8 6v10M32 72V64c0-4 4-6 8-6s8 2 8 6v8M48 72V62c0-4 4-6 8-6s8 2 8 6v10"/>
    </svg>
    <h3>Work as a team</h3>
    <p>Sed ut perspiciatis unde omnis iste natus error sit voluptatem accusantium dolor emque laudantium, totam rem aperiam, eaque ipsa quae ab illo inventore veritatis et quasi architecto beatae vitae dicta sunt explicabo.</p>
  </div>

  <div class="feature" style="left:450px">
    <svg width="80" height="80" viewBox="0 0 80 80" fill="none" stroke="var(--blue)" stroke-width="2.4" stroke-linecap="round">
      <rect x="16" y="6" width="34" height="42" rx="2"/><path d="M22 16h22M22 24h14M22 32h10"/>
      <circle cx="52" cy="46" r="9"/><circle cx="52" cy="46" r="3"/>
      <path d="M30 60l-12 14M30 60l14 10M30 60l20-2"/><circle cx="30" cy="60" r="3"/><circle cx="18" cy="74" r="3"/><circle cx="44" cy="70" r="3"/><circle cx="62" cy="68" r="3"/>
    </svg>
    <h3>Manage from anywhere</h3>
    <p>Sed ut perspiciatis unde omnis iste natus error sit voluptatem accusantium dolor emque laudantium, totam rem aperiam, eaque ipsa quae ab illo inventore veritatis et quasi architecto beatae vitae dicta sunt explicabo.</p>
  </div>

  <div class="feature" style="left:793px">
    <svg width="80" height="80" viewBox="0 0 80 80" fill="none" stroke="var(--blue)" stroke-width="2.4" stroke-linecap="round">
      <rect x="20" y="4" width="40" height="16" rx="2"/><circle cx="40" cy="38" r="10"/><circle cx="40" cy="38" r="4"/>
      <path d="M40 24v4M40 48v4M26 38h4M50 38h4"/><rect x="26" y="58" width="10" height="10"/><rect x="44" y="58" width="10" height="10"/>
      <path d="M12 30v36M8 62l4 4 4-4M68 54V18M64 22l4-4 4 4"/>
    </svg>
    <h3>Automate processes</h3>
    <p>Sed ut perspiciatis unde omnis iste natus error sit voluptatem accusantium dolor emque laudantium, totam rem aperiam, eaque ipsa quae ab illo inventore veritatis et quasi architecto beatae vitae dicta sunt explicabo.</p>
  </div>
</section>

<section class="integrate">
  <div class="art" role="img" aria-label="Illustration of two laptops linked by data lines and service icons" style="left:135px;top:2243px;width:420px;height:452px;background:linear-gradient(135deg,#f0f1f3,var(--blue-5))"></div>
  <h2 class="head abs" style="left:652px;top:2258px;width:400px;font-size:25px;line-height:33.5px">Integrate your maintenance system</h2>
  <div class="rule" style="left:652px;top:2343px"></div>
  <p class="body-copy abs" style="left:652px;top:2382px;width:410px">Sed ut perspiciatis unde omnis iste natus error sit voluptatem accusantium doloremque laudantium, totam rem aperiam, eaque ipsa quae ab illo inventore veritatis et quasi architecto beatae vitae dicta sunt explicabo. Nemo enim ipsam voluptatem quia voluptas sit aspernatur aut odit aut fugit, sed quia consequuntur magni dolores eos qui ratione voluptatem sequi nesciunt. Neque porro quisquam est, qui dolorem ipsum quia dolor sit amet, consectetur, adipisci velit, sed quia non numquam eius modi tempora incidunt ut labore et dolore magnam aliquam quaerat voluptatem</p>
  <a class="btn" style="left:655px;top:2588px;width:107px;height:38px">Read More</a>
</section>

<section class="blog">
  <h2 class="head abs" style="left:0;width:1200px;text-align:center;top:2720px;font-size:25px">Latest Blog</h2>
  <div class="rule" style="left:581px;top:2773px"></div>

  <article class="card" style="left:130px">
    <div class="art" role="img" aria-label="Illustration of a laptop surrounded by cloud and settings icons" style="background:linear-gradient(135deg,var(--blue-5),#e4e8ef)"></div>
    <h4>Lorem ipsum dolor sit amet cons ect etur adipiscing elitsed do</h4>
    <p class="body-copy">Sed ut perspiciatis unde omnis iste natus error sit voluptatem accusantium doloremque laudantium, totam rem aperiam, eaque ipsa quae ab illo inventore veritatis et quasi architecto beatae vitae dicta sunt explicabo. Nemo enim ipsam voluptatem quia voluptas sit aspernatur.</p>
    <a class="btn">Read More</a>
  </article>

  <article class="card" style="left:612px">
    <div class="art" role="img" aria-label="Illustration of a woman planning routes on a map with a clock and plants" style="background:linear-gradient(180deg,var(--blue-4),#dfeee0)"></div>
    <h4>Lorem ipsum dolor sit amet cons ect etur adipiscing elitsed do</h4>
    <p class="body-copy">Sed ut perspiciatis unde omnis iste natus error sit voluptatem accusantium doloremque laudantium, totam rem aperiam, eaque ipsa quae ab illo inventore veritatis et quasi architecto beatae vitae dicta sunt explicabo. Nemo enim ipsam voluptatem quia voluptas sit aspernatur.</p>
    <a class="btn">Read More</a>
  </article>
</section>

<section class="cta">
  <p class="head abs" style="left:0;width:1200px;text-align:center;top:3420px;font-size:17px;text-decoration:underline;text-underline-offset:5px">Ready to get started?</p>
  <h2 class="head abs" style="left:0;width:1200px;text-align:center;top:3478px;font-size:25px;line-height:34px">Join thousands of satisfied<br>customers using Routevia</h2>
  <p class="abs" style="left:0;width:1200px;text-align:center;top:3564px;font-size:15px;line-height:24px;color:var(--ink)">Sed ut perspiciatis unde omnis iste natus error sit voluptatem accusantium<br>doloremque laudantium, totam rem aperiam, eaque ipsa quae</p>
  <a class="btn" style="left:530px;top:3641px;width:140px;height:35px">Start Free Trial</a>
</section>

<footer>
  <div class="band" style="top:3744px;height:340px"></div>
  <div class="brand" style="left:130px;top:3800px;font-size:34px">
    <span class="brand-dot" style="width:80px;height:80px"></span>Routevia
  </div>
  <div class="footer-col abs" style="left:445px;top:3784px">
    <h5>PRODUCTS</h5>
    <ul><li>Fleet maintenance software</li><li>EAM software</li><li>CMMS</li></ul>
  </div>
  <div class="footer-col abs" style="left:699px;top:3784px">
    <h5>COMPANY</h5>
    <ul><li>About</li><li>Pricing</li><li>Careers</li><li>Services</li><li>Accessibility</li><li>Contact</li></ul>
  </div>
  <div class="footer-col abs" style="left:869px;top:3784px">
    <h5>FOLLOW US</h5>
    <div class="social">
      <span style="background:var(--blue)" aria-label="Social profile"></span>
      <span style="background:var(--blue-2)" aria-label="Social profile"></span>
      <span style="background:var(--purple)" aria-label="Social profile"></span>
      <span style="background:var(--purple-2)" aria-label="Social profile"></span>
    </div>
  </div>
  <div class="abs" style="left:130px;top:3987px;width:937px;height:1px;background:var(--line)"></div>
  <p class="abs" style="left:0;width:1200px;text-align:center;top:4029px;font-size:11.5px;color:var(--text)">Copyright © 2023 All Rights Reserved</p>
</footer>

</body>
</html>
```